Kestrel Calisthenics Gym Website

We need a website design for our gym.

Kestrel is the UAE's first calisthenics and parkour gym. The theme under which the gym revolves is that one does not require any machinery to workout as our bodies could be themselves the machinery. The gym is designed to be the more of a social hub rather than an "in-and-out" gym, where people come train, have fun, hang out and socialize for a few hours rather than just train for 60 minutes then leave. The gym is designed to be a big open space with lots of natural sunlight, natural wood and plants all over the place to create a natural and refreshing setting. We also use recycled material throughout the gym and recycle our waste as being green is part of our philosophy. We currently also have some of the world's top and most recognized calisthenics athletes working with us.

We would like our website to reflect all that as well as provide a simple, interactive and fun way for visitors to be able to get class and gym information, check out gym media and contact us for bookings.

Target Market(s)

Ages 15-35

Industry/Entity Type

Fitness

Coding

Coded - Design and coding required

Number of Pages Required

4 page

Font styles to use
Decorative

Colors
0792cd

Requirements
Must have
• Class descriptions
• Gym description
• Class schedules
• Trainer profiles
• Gym philosophy
• Contact Details
Nice to have
• A link to contact us directly for a free first trial class

```html
<!DOCTYPE html>
<html lang="en">
<head>
<meta charset="utf-8">
<title>Kestrel Calisthenics Gym</title>
<link href="https://fonts.googleapis.com/css2?family=Oswald:wght@400;600;700&family=Open+Sans:ital,wght@0,400;0,600;0,700;1,600&display=swap" rel="stylesheet">
<style>
:root{
  --brand:#0792cd;
  --brand-dark:#056a96;
  --ink:#222629;
  --muted:#555b60;
  --band:#eceeef;
  --footer:#202427;
  --footer-deep:#141618;
  --white:#ffffff;
}
*{box-sizing:border-box;margin:0;padding:0}
html,body{width:1200px;height:2416px;overflow:hidden}
body{position:relative;background:var(--white);font-family:"Open Sans",Arial,sans-serif;color:var(--ink)}
.abs{position:absolute}

/* header */
.site-header{left:0;top:0;width:1200px;height:120px;background:var(--white)}
.brand{left:28px;top:14px;display:flex;align-items:center;gap:10px}
.brand-mark{width:18px;height:18px;background:var(--brand);border-radius:50%}
.brand-name{font-family:"Open Sans",sans-serif;font-weight:700;font-size:38px;color:var(--ink);letter-spacing:-1px}
.top-info{right:40px;top:18px;display:flex;gap:34px;font-size:14px;color:var(--muted)}
.top-info span{display:flex;align-items:center;gap:8px}
.main-nav{left:300px;top:72px;width:900px;height:48px;background:var(--brand);display:flex;justify-content:space-around;align-items:center;padding:0 20px}
.main-nav a{color:var(--white);text-decoration:none;font-weight:700;font-size:14px;letter-spacing:.5px}
.main-nav a.active{background:var(--brand-dark);padding:15px 18px}

/* hero */
.hero{left:0;top:120px;width:1200px;height:620px;background:linear-gradient(180deg,#3a3633 0%,#5a4a40 45%,#7a3b2e 75%,#4a2a22 100%)}
.hero-title-box{left:205px;top:290px;width:475px;height:125px;background:rgba(20,20,20,.72);padding:18px 22px}
.hero-title{font-family:"Oswald",sans-serif;font-weight:700;font-size:38px;color:var(--white);line-height:1.1;white-space:nowrap}
.hero-title em{font-style:normal;color:var(--brand)}
.hero-sub{font-family:"Open Sans",sans-serif;font-style:italic;font-weight:600;font-size:28px;color:var(--white);margin-top:8px}
.hero-cta{left:208px;top:428px;width:464px;height:54px;background:var(--brand);color:var(--white);font-family:"Oswald",sans-serif;font-size:32px;display:flex;align-items:center;justify-content:center;letter-spacing:1px}
.join-form{left:820px;top:272px;width:240px;height:300px;background:var(--brand);padding:24px 20px}
.join-form .field{background:var(--white);height:34px;margin-bottom:12px;font-size:12px;color:#8a9095;padding:9px 10px}
.join-form .field.tall{height:70px}
.join-form .submit{margin-left:auto;width:120px;height:38px;background:var(--ink);color:var(--white);font-weight:700;font-size:15px;display:flex;align-items:center;justify-content:center}
.form-badge{left:918px;top:218px;width:60px;height:60px;border-radius:50%;background:var(--ink);border:3px solid var(--white);display:flex;align-items:center;justify-content:center}

/* services */
.services{left:0;top:740px;width:1200px;height:300px;background:var(--band)}
.service{top:60px;width:200px;text-align:center}
.service svg{display:block;margin:0 auto}
.service-label{font-weight:600;font-size:20px;margin-top:22px;color:var(--ink)}

/* welcome */
.welcome-title{left:0;top:1070px;width:1200px;text-align:center;font-family:"Oswald",sans-serif;font-weight:700;font-size:32px;color:var(--ink)}
.welcome-copy{left:110px;top:1128px;width:980px;text-align:center;font-size:13.5px;line-height:1.55;color:var(--muted)}

/* cards */
.card{width:300px;height:270px;background:var(--white);box-shadow:0 1px 4px rgba(0,0,0,.18)}
.card-photo{width:300px;height:170px}
.card-tab{position:absolute;left:60px;top:158px;width:180px;height:26px;background:var(--brand);color:var(--white);font-size:12px;font-weight:700;display:flex;align-items:center;justify-content:center}
.card-text{padding:22px 18px 0;font-size:12px;line-height:1.5;color:var(--muted)}

/* social */
.social{left:0;top:1990px;width:1200px;display:flex;justify-content:center;gap:8px}
.social span{width:40px;height:40px;display:block}

/* footer */
.site-footer{left:0;top:2072px;width:1200px;height:320px;background:var(--footer);color:#c9cdd0}
.footer-col h3{font-family:"Open Sans",sans-serif;font-weight:400;font-size:28px;color:var(--white)}
.footer-col .rule{width:100%;height:4px;background:var(--brand);margin:10px 0 16px}
.footer-col p{font-size:12px;line-height:1.5}
.input{height:30px;background:var(--white);margin-top:12px;width:220px}
.btn-small{margin-top:10px;width:70px;height:24px;background:var(--brand);color:var(--white);font-size:11px;display:flex;align-items:center;justify-content:center}
.news-item{display:flex;gap:12px;margin-bottom:12px}
.news-date{width:40px;height:40px;background:var(--brand);color:var(--white);font-size:10px;display:flex;align-items:center;justify-content:center;text-align:center;line-height:1.1;flex:none}
.contact-row{display:flex;gap:12px;margin-bottom:14px}
.contact-row i{width:10px;height:10px;border-radius:50%;background:var(--brand);margin-top:4px;flex:none}
.contact-row b{color:var(--white);font-size:12px;display:block}
.copyright{left:0;top:2392px;width:1200px;height:24px;background:var(--footer-deep);color:#9aa0a4;font-size:11px;display:flex;align-items:center;justify-content:center}
</style>
</head>
<body>

<header class="site-header abs">
  <div class="brand abs"><span class="brand-mark"></span><span class="brand-name">Kestrel.</span></div>
  <div class="top-info abs">
    <span><svg width="14" height="14" viewBox="0 0 24 24"><path d="M6 2h4l2 5-3 2a12 12 0 006 6l2-3 5 2v4a2 2 0 01-2 2A18 18 0 014 4a2 2 0 012-2z" fill="#0792cd"/></svg>1300 555 010</span>
    <span><svg width="16" height="12" viewBox="0 0 24 18"><rect x="1" y="1" width="22" height="16" fill="none" stroke="#0792cd" stroke-width="2"/><path d="M1 1l11 9 11-9" fill="none" stroke="#0792cd" stroke-width="2"/></svg>contact@kestrel-gym.com</span>
  </div>
  <nav class="main-nav abs">
    <a class="active" href="#">HOME</a><a href="#">ABOUT US</a><a href="#">CLASSES</a><a href="#">TRAINERS</a><a href="#">EVENT</a><a href="#">ELEMENTS</a><a href="#">SHOP</a><a href="#">CONTACT</a>
  </nav>
</header>

<section class="hero abs" role="img" aria-label="Photo of the open gym floor with training equipment"></section>
<div class="hero-title-box abs">
  <div class="hero-title">KESTREL CALISTHENICS <em>GYM</em></div>
  <div class="hero-sub">Achive your Fitness Goals</div>
</div>
<div class="hero-cta abs">GET STARTED TODAY</div>

<form class="join-form abs">
  <div class="field">Name</div>
  <div class="field">Email</div>
  <div class="field">Phone</div>
  <div class="field tall">Message</div>
  <div class="submit">Join Now !</div>
</form>
<div class="form-badge abs">
  <svg width="26" height="26" viewBox="0 0 24 24"><path d="M4 20l1-5L16 4l4 4L9 19z" fill="#fff"/></svg>
</div>

<section class="services abs">
  <div class="service abs" style="left:88px">
    <svg width="120" height="120" viewBox="0 0 120 120"><polygon points="60,4 108,32 108,88 60,116 12,88 12,32" fill="#0792cd"/><circle cx="40" cy="72" r="14" fill="none" stroke="#fff" stroke-width="5"/><circle cx="80" cy="72" r="14" fill="none" stroke="#fff" stroke-width="5"/><path d="M40 72l14-24 12 24h14M54 48h14" fill="none" stroke="#fff" stroke-width="5"/></svg>
    <div class="service-label">CYCLING</div>
  </div>
  <div class="service abs" style="left:400px">
    <svg width="120" height="120" viewBox="0 0 120 120"><polygon points="60,4 108,32 108,88 60,116 12,88 12,32" fill="#fff" stroke="#222629" stroke-width="3"/><circle cx="60" cy="42" r="8" fill="#222629"/><path d="M36 82c10-6 38-6 48 0M60 52v20M44 64l16-6 16 6" fill="none" stroke="#222629" stroke-width="5" stroke-linecap="round"/></svg>
    <div class="service-label">YOGA PILATES</div>
  </div>
  <div class="service abs" style="left:700px">
    <svg width="120" height="120" viewBox="0 0 120 120"><polygon points="60,4 108,32 108,88 60,116 12,88 12,32" fill="#fff" stroke="#222629" stroke-width="3"/><circle cx="40" cy="72" r="14" fill="none" stroke="#222629" stroke-width="5"/><circle cx="80" cy="72" r="14" fill="none" stroke="#222629" stroke-width="5"/><path d="M40 72l14-24 12 24h14M54 48h14" fill="none" stroke="#222629" stroke-width="5"/></svg>
    <div class="service-label">CYCLING</div>
  </div>
  <div class="service abs" style="left:980px">
    <svg width="120" height="120" viewBox="0 0 120 120"><polygon points="60,4 108,32 108,88 60,116 12,88 12,32" fill="#fff" stroke="#222629" stroke-width="3"/><rect x="42" y="36" width="36" height="34" rx="14" fill="none" stroke="#222629" stroke-width="5"/><rect x="46" y="72" width="28" height="14" fill="none" stroke="#222629" stroke-width="5"/></svg>
    <div class="service-label">BOXING</div>
  </div>
</section>

<h1 class="welcome-title abs">WELCOME TO KESTREL GYM</h1>
<p class="welcome-copy abs">Lorem ipsum dolor sit amet, consectetur adipiscing elit, sed do eiusmod tempor incididunt ut labore et dolore magna aliqua. Ut enim ad minim veniam, quis nostrud exercitation ullamco laboris nisi ut aliquip ex ea commodo consequat. Duis aute irure dolor in reprehenderit in voluptate velit esse cillum dolore eu fugiat nulla pariatur. Excepteur sint occaecat cupidatat non proident, sunt in culpa qui officia deserunt mollit anim id est laborum. Sed ut perspiciatis unde omnis iste natus error sit voluptatem accusantium doloremque laudantium, totam rem aperiam, eaque ipsa quae ab illo inventore veritatis et quasi architecto beatae vitae dicta sunt explicabo.</p>

<article class="card abs" style="left:88px;top:1310px">
  <div class="card-photo" role="img" aria-label="Photo of members training in the gym" style="background:linear-gradient(160deg,#c9cfd4,#8e969c)"></div>
  <div class="card-tab">Gym description</div>
  <p class="card-text">We are an independent gym that is committed to working with you to gain the results you want. Whether your aim is to</p>
</article>
<article class="card abs" style="left:450px;top:1310px">
  <div class="card-photo" role="img" aria-label="Photo of a group class on bikes" style="background:linear-gradient(160deg,#7a8a9a,#3c4550)"></div>
  <div class="card-tab">Class descriptions</div>
  <p class="card-text">We are an independent gym that is committed to working with you to gain the results you want. Whether your aim is to</p>
</article>
<article class="card abs" style="left:812px;top:1310px">
  <div class="card-photo" role="img" aria-label="Photo of a class in the studio" style="background:linear-gradient(160deg,#b79a86,#6e5548)"></div>
  <div class="card-tab">Class schedules</div>
  <p class="card-text">We are an independent gym that is committed to working with you to gain the results you want. Whether your aim is to</p>
</article>
<article class="card abs" style="left:88px;top:1640px">
  <div class="card-photo" role="img" aria-label="Photo of an indoor cycling session" style="background:linear-gradient(160deg,#5f6a74,#2c3137)"></div>
  <p class="card-text">We are an independent gym that is committed to working with you to gain the results you want. Whether your aim is to</p>
</article>
<article class="card abs" style="left:450px;top:1640px">
  <div class="card-photo" role="img" aria-label="Photo of members stretching together" style="background:linear-gradient(160deg,#e3e5e7,#a4aab0)"></div>
  <div class="card-tab">Gym philosophy</div>
  <p class="card-text">We are an independent gym that is committed to working with you to gain the results you want. Whether your aim is to</p>
</article>
<article class="card abs" style="left:812px;top:1640px">
  <div class="card-photo" role="img" aria-label="Photo of trainers leading a workout" style="background:linear-gradient(160deg,#c6a99a,#7d6a60)"></div>
  <div class="card-tab">Trainer profiles</div>
  <p class="card-text">We are an independent gym that is committed to working with you to gain the results you want. Whether your aim is to</p>
</article>

<div class="social abs" aria-label="Social links">
  <span style="background:#3b5998"></span><span style="background:#1da1f2"></span><span style="background:#dd4b39"></span><span style="background:#0077b5"></span><span style="background:#e1306c"></span><span style="background:#ff6600"></span><span style="background:#cb2027"></span>
</div>

<footer class="site-footer abs">
  <div class="footer-col abs" style="left:88px;top:30px;width:280px">
    <h3>Newsletter Signup</h3>
    <div class="rule"></div>
    <p>Sign up for our newsletter and get the latest news.</p>
    <div class="input"></div>
    <div class="btn-small">Subscribe</div>
  </div>
  <div class="footer-col abs" style="left:470px;top:30px;width:260px">
    <h3>News</h3>
    <div class="rule"></div>
    <div class="news-item"><div class="news-date">12<br>May</div><p>Lorem ipsum is dummy.<br>Lorem ipsum is simply dummy</p></div>
    <div class="news-item"><div class="news-date">08<br>May</div><p>Lorem ipsum is dummy.<br>Lorem ipsum is simply dummy</p></div>
    <div class="news-item"><div class="news-date">02<br>May</div><p>Lorem ipsum is dummy.<br>Lorem ipsum is simply dummy</p></div>
  </div>
  <div class="footer-col abs" style="left:810px;top:30px;width:300px">
    <h3>Contacts</h3>
    <div class="rule"></div>
    <div class="contact-row"><i></i><p><b>OPENING HOURS:</b>Monday–Friday 6:00–22:00<br>Saturday 8:00–20:00<br>Sunday 9:00–18:00</p></div>
    <div class="contact-row"><i></i><p><b>ADDRESS:</b>14 Harbour Lane, Unit 3<br>Marina District</p></div>
    <div class="contact-row"><i></i><p><b>TELEPHONE:</b>1300 555 010</p></div>
  </div>
</footer>
<div class="copyright abs">© Copyright 2014 - KESTREL GYM All Right Reserved</div>

</body>
</html>
```